" Empresa que trabalha com danças urbanas. Workhops, Batalhas, Performances, Palestras, Bate-papos, Jam Sessions. Também possui um projeto social em comunidades. "

```html
<!DOCTYPE html>
<html lang="pt-BR">
<head>
<meta charset="utf-8">
<title>Ritmo Urbano — Danças Urbanas</title>
<link href="https://fonts.googleapis.com/css2?family=Oswald:wght@500;700&family=Roboto+Condensed:wght@400;700&family=Open+Sans:wght@400;600&display=swap" rel="stylesheet">
<style>
:root{
  --page:#ffffff;
  --ink-dark:#1c1c1c;
  --panel:#2a2a2a;
  --panel-line:#333;
  --silver-hi:#f2f2f2;
  --silver-lo:#9a9a9a;
  --card:#c9c9c9;
  --card-ink:#222;
  --accent:#6b8e23;
  --accent-dark:#3e5a12;
  --nav:#d8d8d8;
  --muted:#bbbbbb;
}
*{box-sizing:border-box;margin:0;padding:0}
html,body{width:1200px;height:1200px;overflow:hidden;background:var(--page)}
body{position:relative;font-family:"Open Sans",sans-serif;color:var(--card-ink)}
.site{position:absolute;left:187px;top:0;width:826px;height:1178px;background:
  repeating-linear-gradient(45deg,#2d2d2d 0 3px,#262626 3px 6px);overflow:hidden}
.abs{position:absolute}

/* header */
.masthead{left:0;top:0;width:826px;height:96px;background:linear-gradient(180deg,#5a5a5a,#2b2b2b 70%,#1e1e1e)}
.masthead::after{content:"";position:absolute;left:0;right:0;bottom:0;height:4px;background:var(--accent)}
.lang{left:14px;top:14px;display:flex;gap:6px}
.lang span{width:24px;height:15px;background:#bdbdbd;border:1px solid #eee}
.battle-note{left:80px;top:10px;width:104px;height:46px;background:#f4f4f4;border-radius:3px;font:600 8.5px/1.25 "Open Sans",sans-serif;color:#333;padding:5px 6px;text-align:center}
.battle-note b{display:block;margin-top:3px;background:#222;color:#fff;font-size:7px;padding:2px 0;border-radius:2px}
.brand{left:323px;top:12px;width:180px;height:62px;display:flex;align-items:center;justify-content:center;gap:8px;font:700 24px "Oswald",sans-serif;color:#fff;letter-spacing:1px}
.brand i{width:14px;height:14px;background:var(--accent);display:block}
.social{display:flex;gap:4px}
.social span{width:13px;height:13px;background:#e6e6e6;border-radius:2px}
.head-social{left:555px;top:28px}
.dancer-art{right:20px;top:8px;width:80px;height:84px;background:radial-gradient(circle at 50% 50%,#111 0 35%,transparent 60%)}

/* nav */
.nav{left:0;top:96px;width:826px;height:19px;background:linear-gradient(180deg,#eee,var(--nav));display:flex;justify-content:center;gap:18px;align-items:center;font:700 9px "Roboto Condensed",sans-serif;color:#555;letter-spacing:.5px}
.nav .on{color:#111}
.subnav{left:0;top:115px;width:826px;height:17px;background:#1a1a1a;display:flex;justify-content:center;gap:4px;font:400 8.5px "Roboto Condensed",sans-serif;color:#ccc}
.subnav span{padding:3px 12px}
.subnav .on{background:var(--accent);color:#fff}

/* team */
.team{left:118px;top:156px;width:600px;height:180px}
.member{position:absolute;top:0;width:148px;height:180px}
.member .photo{position:absolute;left:14px;top:0;width:136px;height:144px;transform:skewX(-10deg);border:2px solid #ddd}
.member:nth-child(1) .photo{background:linear-gradient(135deg,#a0522d,#d9a066 50%,#4a4a4a)}
.member:nth-child(2) .photo{background:linear-gradient(135deg,#9a9a9a,#5e5e5e)}
.member:nth-child(3) .photo{background:linear-gradient(135deg,#b0b0b0,#3f3f3f)}
.member:nth-child(4) .photo{background:linear-gradient(135deg,#8c8c8c,#2f2f2f)}
.member .name{position:absolute;left:0;top:146px;width:150px;height:34px;background:linear-gradient(180deg,#fff,#cfcfcf);transform:skewX(-10deg);font:400 italic 17px "Roboto Condensed",sans-serif;color:#333;display:flex;align-items:center;justify-content:center}
.member .name.lead{font-weight:700;color:#111}

.intro{left:113px;top:360px;width:600px;height:132px;background:var(--card);border-radius:12px;padding:18px 30px;font:400 10px/1.55 "Open Sans",sans-serif;color:#333}
.intro::before{content:"";position:absolute;left:40px;top:-12px;border:12px solid transparent;border-top:0;border-bottom-color:var(--card)}

/* section bars */
.bar{height:36px;background:linear-gradient(180deg,var(--silver-hi),var(--silver-lo));clip-path:polygon(0 0,100% 0,94% 100%,0 100%);font:700 15px "Roboto Condensed",sans-serif;color:#222;display:flex;align-items:center;justify-content:center;letter-spacing:.5px}
.bar.right{clip-path:polygon(6% 0,100% 0,100% 100%,0 100%)}

.prices{left:101px;top:576px;width:288px;height:139px;background:var(--card);border-radius:0 0 12px 12px;padding:20px 30px;font:700 12px "Roboto Condensed",sans-serif}
.prices li{list-style:none;display:flex;justify-content:flex-end;gap:12px;margin-bottom:10px}
.prices .val{width:72px;font:700 15px "Roboto Condensed",sans-serif;color:#444}
.prices .val small{font-size:8px}

.pay{height:79px;top:605px;background:var(--card);border-radius:10px;text-align:center;padding-top:10px}
.pay h4{font:700 11px "Roboto Condensed",sans-serif;text-decoration:underline;margin-bottom:4px}
.pay p{font:400 7.5px/1.4 "Open Sans",sans-serif}
.cards{display:flex;gap:3px;justify-content:center;margin-top:8px}
.cards span{width:14px;height:9px;background:#777;border-radius:1px}

/* location */
.addr{display:flex;align-items:center;gap:8px;font:700 9px/1.3 "Roboto Condensed",sans-serif;color:#eee;text-transform:uppercase}
.map{left:41px;top:852px;width:372px;height:156px;background:linear-gradient(135deg,#e6e2d6,#cfd8c4 55%,#bcd0e0)}
.map-card{left:198px;top:862px;width:200px;height:126px;background:#fff;opacity:.85;border-radius:2px}

.cta{left:528px;width:168px;height:72px;background:linear-gradient(180deg,#eee,#a9a9a9);border:2px solid #ddd;border-radius:8px;text-align:center;padding-top:8px}
.cta strong{display:block;font:700 24px/1.1 "Oswald",sans-serif;color:#222}
.cta span{font:400 6.5px "Open Sans",sans-serif;color:#333;text-transform:uppercase}

.to-top{left:765px;top:1008px;width:24px;height:24px;background:#ddd;border-radius:3px}

/* footer */
.foot-bar{left:0;top:1037px;width:826px;height:19px;background:linear-gradient(180deg,#f0f0f0,#a8a8a8)}
.foot-social{left:373px;top:1040px}
.foot-info{left:0;top:1060px;width:826px;text-align:center;font:400 7px/1.5 "Open Sans",sans-serif;color:var(--muted)}
.thumbs{left:333px;top:1090px;display:flex;gap:3px}
.thumbs span{width:26px;height:22px;background:linear-gradient(135deg,#777,#444)}
.copyright{left:0;top:1160px;width:826px;height:18px;background:#111;font:400 6.5px/18px "Open Sans",sans-serif;color:#999;text-align:center}
</style>
</head>
<body>
<div class="site">
  <header class="abs masthead">
    <div class="abs lang"><span></span><span></span></div>
    <div class="abs battle-note">Saiba de batalhas pelo Ritmo Urbano<b>CADASTRE-SE</b></div>
    <div class="abs brand"><i></i>Ritmo Urbano</div>
    <div class="abs social head-social"><span></span><span></span><span></span><span></span></div>
    <div class="abs dancer-art" role="img" aria-label="Silhueta de dançarino em movimento"></div>
  </header>

  <nav class="abs nav">
    <span>HOME</span><span class="on">SOBRE</span><span>EVENTOS</span><span>PROJETO SOCIAL</span><span>PARCEIROS</span><span>CURSOS</span><span>EQUIPE</span><span>SHOP</span><span>NEWS</span><span>CONTATO</span>
  </nav>
  <div class="abs subnav"><span class="on">Apresentação</span><span>Staff 2013</span><span>Staff 2012</span><span>Staff 2011</span></div>

  <section class="abs team">
    <div class="member" style="left:0"><div class="photo" role="img" aria-label="Foto de dançarino em passo de breaking"></div><div class="name lead">Marcos Lima</div></div>
    <div class="member" style="left:150px"><div class="photo" role="img" aria-label="Foto de dançarino em freeze"></div><div class="name">Fulano de tal</div></div>
    <div class="member" style="left:300px"><div class="photo" role="img" aria-label="Foto de dançarino em apresentação"></div><div class="name">Beltrano</div></div>
    <div class="member" style="left:450px"><div class="photo" role="img" aria-label="Foto de dançarina em pose"></div><div class="name">Ciclano</div></div>
  </section>

  <p class="abs intro">Lorem Ipsum é simplesmente uma simulação de texto da indústria tipográfica e de impressos, e vem sendo utilizado desde o século XVI, quando um impressor desconhecido pegou uma bandeja de tipos e os embaralhou para fazer um livro de modelos de tipos. Lorem Ipsum sobreviveu não só a cinco séculos, como também ao salto para a editoração eletrônica, permanecendo essencialmente inalterado. Se popularizou na década de 60, quando a Tipográfica Nova lançou decalques contendo passagens de Lorem Ipsum, e mais recentemente quando passou a ser integrado a softwares de editoração eletrônica como o Paginador Pro.</p>

  <div class="abs bar" style="left:41px;top:540px;width:360px">VALORES</div>
  <ul class="abs prices">
    <li>Pacote Simples <span>—</span><span class="val">R$ 35,<small>00</small></span></li>
    <li>Pacote Master <span>—</span><span class="val">R$ 50,<small>00</small></span></li>
    <li>Aula avulsa <span>—</span><span class="val">R$ 20,<small>00</small></span></li>
  </ul>

  <div class="abs bar right" style="left:425px;top:540px;width:360px">FORMAS DE PAGAMENTO</div>
  <div class="abs pay" style="left:433px;width:160px"><h4>Depósito em conta</h4><p>Agência 0000-0<br>Conta Corrente 00000-0<br>Marcos Lima da Costa</p></div>
  <div class="abs pay" style="left:605px;width:161px"><h4>Pagamento Online</h4><div class="cards"><span></span><span></span><span></span><span></span><span></span><span></span></div></div>

  <div class="abs bar" style="left:41px;top:756px;width:360px">LOCALIZAÇÃO</div>
  <div class="abs addr" style="left:41px;top:812px">
    <svg width="14" height="18" viewBox="0 0 14 18"><path d="M7 0a7 7 0 0 0-7 7c0 5 7 11 7 11s7-6 7-11a7 7 0 0 0-7-7z" fill="#eee"/><circle cx="7" cy="7" r="2.5" fill="#2a2a2a"/></svg>
    <span>Endereço completo, CEP 00000-000<br>Rua Fulano de Tal, Nº 123</span>
  </div>
  <div class="abs addr" style="left:240px;top:812px">
    <svg width="14" height="18" viewBox="0 0 14 18"><rect x="1" y="0" width="12" height="13" rx="3" fill="#eee"/><rect x="3" y="3" width="8" height="4" fill="#2a2a2a"/><path d="M3 18l2-4M11 18l-2-4" stroke="#eee" stroke-width="2"/></svg>
    <span>Próximo à estação de<br>Metrô Vila Nova</span>
  </div>
  <div class="abs map" role="img" aria-label="Mapa da localização do estúdio"></div>
  <div class="abs map-card" role="img" aria-label="Vista da rua do estúdio"></div>

  <div class="abs cta" style="top:828px"><strong>INSCRIÇÃO</strong><span>Clique aqui para fazer sua inscrição</span></div>
  <div class="abs cta" style="top:917px"><strong>CRONOGRAMA</strong><span>Clique aqui para ver o nosso cronograma</span></div>
  <svg class="abs to-top" viewBox="0 0 24 24"><rect width="24" height="24" rx="3" fill="#ddd"/><path d="M6 15l6-6 6 6" stroke="#222" stroke-width="3" fill="none"/></svg>

  <div class="abs foot-bar"></div>
  <div class="abs social foot-social"><span></span><span></span><span></span><span></span></div>
  <p class="abs foot-info">Ritmo Urbano © 2013 Todos os direitos reservados<br>Danças urbanas, batalhas e projeto social</p>
  <div class="abs thumbs" role="img" aria-label="Miniaturas de fotos de eventos"><span></span><span></span><span></span><span></span><span></span><span></span></div>
  <p class="abs copyright">Copyright © 2013 Ritmo Urbano — Todos os direitos reservados</p>
</div>
</body>
</html>
```